KVL Accounting Firm Needs Graphic Art for Our Proven Processes and For Our Core Values

**Looking for redesign of attached Powerpoint content (see below)
***Final graphic should be good for web use

Date: March 10, 2017

From: Dalton Esterby, CPA
Esterby, Lundqvist & Associates, P.C. (KVL)

Background:

KVL is a 20 person Houston based CPA firm, providing tax, accounting, financial and consulting services, to individuals and to entrepreneurs and their businesses. KVL is engaged in a process called QPT (See the book Bedrock, by Alden Forsberg) whereby we implement a “system” to operate our company. As part of this system we have defined what we call our “Proven Process”. This is something we will show all prospective clients, and have on our website, that explains what it looks like to work with us. Starting at the beginning of the project to completion.

Project Description:

KVL is looking for graphic artist assistance in designing the following pieces:

1. Graphic depiction of “The KVL Way”, otherwise known as our “Proven Process”. The first attachments labeled KVL will show what we have done ourselves. These will show the general steps we have defined in both a sort of graphic way and a step by step narrative. The second attachment shows you some actual examples other firms have put together, hopefully that will show you what we are asking you to develop for us. Note that we are very open to any suggested clarifications or improvements to what we have done which may include changing phrases or saying something in a different way. Remember we are accountants!

2. We have defined our core values as a company, and we are wanting to develop some posters/placards so we can post them in our conference rooms, break room, etc. Attached are our core values as well as some deeper narratives about what they mean. Also included are many of the “words” we kicked around before arriving at our core values.

3. You will also find an attachment with our logo that should be incorporated, as well. Designs SHOULD INCLUDE, but not be limited to, the colors on our logo. Our end product should reflect a strong sense of our core values.

We would like to have the project in a form that would give us the option to use any/all of the information on our website, posters, brochures, etc.

Thanks in advance for your assistance.
Updates

Project Deadline Extended Reason: We are in the midst of tax deadlines so need a little more time to review and respond. Added Monday, March 20, 2017

Target Market(s)

Entrepreneurs and their companies with revenue greater than one million; Industries such as real estate, construction, trades and professional services; all in the Greater Houston Texas area

Industry/Entity Type

Accounting

Font styles to use
Serif
Other font styles liked:
• We are okay with Serif but are open.

Requirements
Must have
• Proven Process must be presented in a way that is clear and makes sense.
Nice to have
• Clean lines
• Colors should go with logo (see attached)
Should not have
• Can't think of anything - unless I see it

```html
<!DOCTYPE html>
<html lang="en">
<head>
<meta charset="utf-8">
<title>Client Service Approach — Esterby, Lundqvist &amp; Associates, PC</title>
<link href="https://fonts.googleapis.com/css2?family=Open+Sans:wght@800&family=Source+Sans+3:wght@400;600;700&family=EB+Garamond:wght@400&display=swap" rel="stylesheet">
<style>
  :root {
    --header-top: #454545;
    --header-bottom: #232323;
    --header-text: #ffffff;
    --body-bg: #ffffff;
    --ink: #111111;
    --ink-soft: #333333;
    --icon-blue: #2b8ad3;
    --footer-light: #ffffff;
    --footer-dark: #e4e4e4;
    --footer-rule: #c8c8c8;
    --brand-ink: #3c3a2a;
    --brand-gold: #a8934a;
  }
  * { box-sizing: border-box; margin: 0; padding: 0; }
  html, body { width: 1200px; height: 675px; overflow: hidden; background: var(--body-bg); }
  .slide { position: relative; width: 1200px; height: 675px; background: var(--body-bg); overflow: hidden; }

  .slide-header {
    position: absolute; inset: 0 0 auto 0; height: 65px;
    background: linear-gradient(90deg, var(--header-top), var(--header-bottom));
  }
  .slide-title {
    position: absolute; left: 29px; top: 9px;
    font-family: "Open Sans", sans-serif; font-weight: 800;
    font-size: 35px; letter-spacing: 0.2px; color: var(--header-text);
    text-shadow: 0 1px 2px rgba(0,0,0,.35);
  }

  .step-list { position: absolute; list-style: none; top: 178px; width: 520px; }
  .step-list--left { left: 103px; }
  .step-list--right { left: 663px; }
  .step { display: flex; align-items: center; height: 50px; margin-bottom: 25px; }
  .step-icon { width: 50px; height: 50px; flex: none; }
  .step-icon circle.ring { fill: none; stroke: var(--icon-blue); stroke-width: 1.1; }
  .step-icon .glyph { fill: none; stroke: var(--icon-blue); stroke-width: 1.1; stroke-linecap: round; stroke-linejoin: round; }
  .step-copy { margin-left: 28px; font-family: "Source Sans 3", sans-serif; line-height: 25px; }
  .step-name { font-weight: 700; font-size: 19.5px; color: var(--ink); }
  .step-detail { font-weight: 400; font-size: 19.5px; color: var(--ink-soft); }

  .slide-footer {
    position: absolute; left: 0; right: 0; bottom: 0; height: 87px;
    background: linear-gradient(90deg, var(--footer-light) 25%, var(--footer-dark));
    border-top: 1px solid var(--footer-rule);
    box-shadow: 0 -1px 3px rgba(0,0,0,.12);
  }
  .brand { position: absolute; left: 27px; top: 26px; display: flex; align-items: center; gap: 9px; }
  .brand-mark { width: 14px; height: 14px; background: var(--brand-gold); }
  .brand-name { font-family: "EB Garamond", serif; font-weight: 400; font-size: 16px; color: var(--brand-ink); }
</style>
</head>
<body>
<main class="slide">
  <header class="slide-header">
    <h1 class="slide-title">CLIENT SERVICE APPROACH</h1>
  </header>

  <ol class="step-list step-list--left">
    <li class="step">
      <svg class="step-icon" viewBox="0 0 50 50" aria-hidden="true"><circle class="ring" cx="25" cy="25" r="24"/><path class="glyph" d="M14 25l7 7 15-15"/></svg>
      <div class="step-copy"><div class="step-name">Philosophical match</div><div class="step-detail">Initial meeting to determine compatibility</div></div>
    </li>
    <li class="step">
      <svg class="step-icon" viewBox="0 0 50 50" aria-hidden="true"><circle class="ring" cx="25" cy="25" r="24"/><path class="glyph" d="M12 16h26v15H24l-6 5v-5h-6z"/></svg>
      <div class="step-copy"><div class="step-name">Understand your needs</div><div class="step-detail">Client questionnaire / initial meeting</div></div>
    </li>
    <li class="step">
      <svg class="step-icon" viewBox="0 0 50 50" aria-hidden="true"><circle class="ring" cx="25" cy="25" r="24"/><g class="glyph"><circle cx="15" cy="17" r="1.6"/><circle cx="15" cy="25" r="1.6"/><circle cx="15" cy="33" r="1.6"/><path d="M20 17h16M20 25h16M20 33h16"/></g></svg>
      <div class="step-copy"><div class="step-name">Set expectations</div><div class="step-detail">Engagement letter</div></div>
    </li>
    <li class="step">
      <svg class="step-icon" viewBox="0 0 50 50" aria-hidden="true"><circle class="ring" cx="25" cy="25" r="24"/><g class="glyph"><ellipse cx="25" cy="30" rx="14" ry="5"/><circle cx="25" cy="19" r="3.2"/><circle cx="17" cy="22" r="2.8"/><circle cx="33" cy="22" r="2.8"/><path d="M20 30c0-4 2-7 5-7s5 3 5 7M12.5 30c0-3 2-5 4.5-5M37.5 30c0-3-2-5-4.5-5"/></g></svg>
      <div class="step-copy"><div class="step-name">Assign client service staff</div><div class="step-detail">Personal contact within 48 hours</div></div>
    </li>
  </ol>

  <ol class="step-list step-list--right" start="5">
    <li class="step">
      <svg class="step-icon" viewBox="0 0 50 50" aria-hidden="true"><circle class="ring" cx="25" cy="25" r="24"/><g class="glyph"><circle cx="25" cy="20" r="7"/><circle cx="20.5" cy="27.5" r="7"/><circle cx="29.5" cy="27.5" r="7"/><circle cx="25" cy="25" r="12"/></g></svg>
      <div class="step-copy"><div class="step-name">Deeper dive</div><div class="step-detail">Request additional information</div></div>
    </li>
    <li class="step">
      <svg class="step-icon" viewBox="0 0 50 50" aria-hidden="true"><circle class="ring" cx="25" cy="25" r="24"/><g class="glyph"><rect x="16" y="13" width="18" height="24"/><path d="M21 20h8M21 24h8"/></g></svg>
      <div class="step-copy"><div class="step-name">Draft of tax return</div><div class="step-detail">Within 10 bysiness days of receiving all data</div></div>
    </li>
    <li class="step">
      <svg class="step-icon" viewBox="0 0 50 50" aria-hidden="true"><circle class="ring" cx="25" cy="25" r="24"/><g class="glyph"><rect x="13" y="13" width="24" height="24"/><rect x="16" y="16" width="8" height="6"/><path d="M26 17h8M26 20h8M16 25h18M16 28h18M16 31h10M28 36l8-8"/></g></svg>
      <div class="step-copy"><div class="step-name">File tax return</div><div class="step-detail">Your preference: hard copy / pdf</div></div>
    </li>
    <li class="step">
      <svg class="step-icon" viewBox="0 0 50 50" aria-hidden="true"><circle class="ring" cx="25" cy="25" r="24"/><g class="glyph"><rect x="14" y="14" width="22" height="22"/><path d="M19 25l4 4 8-9"/></g></svg>
      <div class="step-copy"><div class="step-name">Review outcomes</div><div class="step-detail">Determine if your expectations were met</div></div>
    </li>
  </ol>

  <footer class="slide-footer">
    <div class="brand">
      <span class="brand-mark" aria-hidden="true"></span>
      <span class="brand-name">Esterby, Lundqvist &amp; Associates, PC</span>
    </div>
  </footer>
</main>
</body>
</html>
```